Software - upgrade look and feel

Brightwell Tallyworks is the worldwide distributor of the zLumio software application, which powers a loan strategy as described at www.brightwelltallyworks.com.The company has recently upgraded its image and website; and now seeks to give zLumio a much-needed face-lift.Using the screen shots of the existing application (2 x screens provided), recreate the screens in a modern and vibrant style that generates a feeling of professionalism and confidence.

Target Market(s)

Financial services industry and their clients.

Industry/Entity Type

Financial Service

Font styles to use
Other font styles liked:
• See our website at brightwelltallyworks.com - happy with this font, but open to ideas.

Colors

Designer to choose colors to be used in the design.

Requirements
Must have
• Existing fields, but perhaps more intuitive for the User.
Nice to have
• A less busy look that suggests an innovative software application.
Should not have
• Complication.

```html
<!DOCTYPE html>
<html lang="en">
<head>
<meta charset="utf-8">
<title>zLumio – Calculate</title>
<link href="https://fonts.googleapis.com/css2?family=Rubik:wght@400;500&display=swap" rel="stylesheet">
<style>
:root{
  --bg:#f7f9fc;
  --panel:#ffffff;
  --ink:#3a4356;
  --ink-soft:#5c6577;
  --blue:#168fe9;
  --blue-deep:#0f86e0;
  --red:#f7727b;
  --line:#1a8fe6;
  --axis:#4a5263;
}
*{box-sizing:border-box;margin:0;padding:0}
html,body{width:1200px;height:934px;overflow:hidden;background:var(--bg)}
body{position:relative;font-family:'Rubik',sans-serif;color:var(--ink)}

.sidebar{position:absolute;left:0;top:80px;width:222px}
.nav-item{position:absolute;left:0;width:222px;height:44px;display:flex;align-items:center;padding-left:18px;font-size:13.5px;color:var(--ink)}
.nav-item svg{width:18px;height:18px;margin-right:14px;fill:none;stroke:var(--blue);stroke-width:1.8;stroke-linecap:round;stroke-linejoin:round}
.nav-item.active{background:var(--panel);border-right:3px solid var(--blue)}
.n1{top:3px}.n2{top:53px}.n3{top:99px}.n4{top:148px}.n5{top:198px}

.heading{position:absolute;top:30px;font-size:17.5px;font-weight:500;color:var(--ink)}
.heading.general{left:235px}
.heading.client{right:51px}
.heading.client span{color:var(--blue)}

.label{position:absolute;font-size:13.5px;color:var(--ink);line-height:30px}
.input{position:absolute;height:31px;background:var(--panel);border:1.5px solid var(--line);border-radius:2px;font-size:12.5px;color:var(--ink-soft);line-height:28px;padding-left:14px}
.input svg{position:absolute;right:12px;top:10px;width:11px;height:8px;fill:none;stroke:var(--blue);stroke-width:1.8}
.col-l-label{left:235px}
.col-l{left:337px;width:316px}
.col-r-label{left:731px}
.col-r{left:834px;width:316px}
.col-r-short{left:834px;width:182px}
.r1{top:72px}.r2{top:119px}.r3{top:166px}.r4{top:213px}
.r5{top:525px}.r6{top:572px}.r7{top:672px}.r8{top:719px}

.link{position:absolute;font-size:13.5px;color:var(--blue);text-decoration:underline;line-height:30px}
.link.additional{right:51px;top:72px}
.link.statistics{left:900px;top:255px}
.link.pending{right:51px;top:255px}
.link.report{left:235px;top:807px}

.chart{position:absolute;left:230px;top:295px;width:930px;height:180px}
.chart text{font-family:'Rubik',sans-serif;font-size:12.5px;fill:var(--ink-soft)}

.legend{position:absolute;top:475px;display:flex;align-items:center;font-size:13.5px;color:var(--ink)}
.legend i{display:block;width:26px;height:26px;border-radius:3px;margin-right:22px}
.legend.step3{left:909px}.legend.step3 i{background:var(--blue)}
.legend.step4{left:1057px}.legend.step4 i{background:var(--red)}

.button{position:absolute;top:805px;height:34px;width:104px;font-size:12.5px;font-weight:500;letter-spacing:.6px;display:flex;align-items:center;justify-content:center;border-radius:2px}
.button.save{left:927px;background:var(--blue);color:#fff}
.button.cancel{left:1046px;border:1.5px solid var(--line);color:var(--blue-deep);background:var(--panel)}
</style>
</head>
<body>

<nav class="sidebar">
  <div class="nav-item n1"><svg viewBox="0 0 18 18"><circle cx="9" cy="5.5" r="3.5"/><path d="M2.5 17c0-4 3-6.5 6.5-6.5s6.5 2.5 6.5 6.5"/></svg>Client / Income</div>
  <div class="nav-item n2"><svg viewBox="0 0 18 18"><path d="M1.5 13.5l5-5 3.5 3.5 6-6.5"/><path d="M12 5.5h4v4"/></svg>Expneses</div>
  <div class="nav-item n3"><svg viewBox="0 0 18 18"><rect x="1.5" y="5" width="15" height="11" rx="1"/><path d="M6 5V2.5h6V5M6 5v11M12 5v11"/></svg>Assets / Liablities</div>
  <div class="nav-item n4"><svg viewBox="0 0 18 18"><path d="M2 4.5h14M2 9h14M2 13.5h14"/><circle cx="6" cy="4.5" r="1.6"/><circle cx="12" cy="9" r="1.6"/><circle cx="7" cy="13.5" r="1.6"/></svg>Restructure</div>
  <div class="nav-item n5 active"><svg viewBox="0 0 18 18"><circle cx="9" cy="9" r="7"/><path d="M9 2v7h7"/></svg>Calculate</div>
</nav>

<h1 class="heading general">General Information</h1>
<h2 class="heading client">Client: <span>Peter and Anna Vale</span></h2>

<div class="label col-l-label r1">View</div>
<div class="input col-l r1">Client 1<svg viewBox="0 0 11 8"><path d="M1 1.5l4.5 4.5 4.5-4.5"/></svg></div>
<div class="label col-l-label r2">Loan Writer</div>
<div class="input col-l r2">Harlan, Martin (555-0142678)<svg viewBox="0 0 11 8"><path d="M1 1.5l4.5 4.5 4.5-4.5"/></svg></div>
<div class="label col-l-label r3">CS Officer</div>
<div class="input col-l r3">Harlan, Martin (555-0142678)<svg viewBox="0 0 11 8"><path d="M1 1.5l4.5 4.5 4.5-4.5"/></svg></div>
<div class="label col-l-label r4">File No.</div>
<div class="input col-l r4">1234-998629-901</div>

<div class="label col-r-label r1">Title</div>
<div class="input col-r-short r1">Client Title</div>
<a class="link additional">Additional Info</a>
<div class="label col-r-label r2">Family Name</div>
<div class="input col-r r2">Vale<svg viewBox="0 0 11 8"><path d="M1 1.5l4.5 4.5 4.5-4.5"/></svg></div>
<div class="label col-r-label r3">First Name</div>
<div class="input col-r r3">Peter<svg viewBox="0 0 11 8"><path d="M1 1.5l4.5 4.5 4.5-4.5"/></svg></div>
<div class="label col-r-label r4">Email</div>
<div class="input col-r r4">peteranna@sampleinbox.com</div>

<a class="link statistics">Statistics</a>
<a class="link pending">Send to Pending Tray</a>

<svg class="chart" viewBox="230 295 930 180" role="img" aria-label="Balance over term in years, Step 3 and Step 4">
  <path fill="var(--red)" d="M327.5 405 C365 405 365 376 402 376 C420 376 420 382 439 382 C476 382 476 391 514 391 C541 391 541 382 569 382 C590 382 590 364 610 364 C623 364 623 382 636 382 C649 382 649 382 662 382 C705 382 705 311 748 311 C770 311 770 335 792 335 C813 335 813 371 834 371 C887 371 887 345 941 345 C954 345 954 352 968 352 C986 352 986 385 1005 385 C1029 385 1029 371 1054 371 C1081 371 1081 362 1109 362 C1127 362 1127 405 1146 405 Z"/>
  <path fill="var(--blue)" fill-opacity=".92" d="M327.5 405 C365 405 365 389 402 389 C430 389 430 395 458 395 C486 395 486 397 514 397 C541 397 541 390 569 390 C590 390 590 364 610 364 C623 364 623 387 636 387 C649 387 649 385 662 385 C705 385 705 321 748 321 C770 321 770 347 792 347 C813 347 813 379 834 379 C884 379 884 350 934 350 C951 350 951 356 968 356 C988 356 988 387 1009 387 C1027 387 1027 379 1045 379 C1062 379 1062 360 1079 360 C1100 360 1100 375 1120 375 C1133 375 1133 405 1146 405 Z"/>
  <g stroke="var(--axis)" stroke-width="1.2">
    <path d="M306 310h9M306 333.5h9M306 357h9M306 381h9M306 405h9"/>
    <path d="M327.5 408v9M364.7 408v9M401.9 408v9M439.2 408v9M476.4 408v9M513.6 408v9M550.8 408v9M588 408v9M625.3 408v9M662.5 408v9M699.7 408v9M736.9 408v9M774.1 408v9M811.4 408v9M848.6 408v9M885.8 408v9M923 408v9M960.2 408v9M997.5 408v9M1034.7 408v9M1071.9 408v9M1109.1 408v9M1146.3 408v9"/>
    <path d="M327.5 414H1146.3"/>
  </g>
  <g text-anchor="end">
    <text x="300" y="314">40,000</text><text x="300" y="338">30,000</text><text x="300" y="361">20,000</text><text x="300" y="385">10,000</text><text x="300" y="409">5,000</text>
  </g>
  <text x="248" y="357" transform="rotate(-90 248 357)" text-anchor="middle">Balance</text>
  <g text-anchor="middle">
    <text x="327.5" y="440">0</text><text x="364.7" y="440">1</text><text x="401.9" y="440">2</text><text x="439.2" y="440">3</text><text x="476.4" y="440">4</text><text x="513.6" y="440">5</text><text x="550.8" y="440">6</text><text x="588" y="440">7</text><text x="625.3" y="440">8</text><text x="662.5" y="440">9</text><text x="699.7" y="440">10</text><text x="736.9" y="440">11</text><text x="774.1" y="440">12</text><text x="811.4" y="440">13</text><text x="848.6" y="440">14</text><text x="885.8" y="440">15</text><text x="923" y="440">16</text><text x="960.2" y="440">17</text><text x="997.5" y="440">18</text><text x="1034.7" y="440">19</text><text x="1071.9" y="440">20</text><text x="1109.1" y="440">21</text><text x="1146.3" y="440">22</text>
    <text x="737" y="462">Term (years)</text>
  </g>
</svg>

<div class="legend step3"><i></i>Step 3</div>
<div class="legend step4"><i></i>Step 4</div>

<div class="label col-l-label r5">Graph Type</div>
<div class="input col-l r5">Years / Interest Saved<svg viewBox="0 0 11 8"><path d="M1 1.5l4.5 4.5 4.5-4.5"/></svg></div>
<div class="label col-l-label r6">Analysis</div>
<div class="input col-l r6">Analysis by Year<svg viewBox="0 0 11 8"><path d="M1 1.5l4.5 4.5 4.5-4.5"/></svg></div>

<a class="link col-l-label r7">Years Saved</a>
<div class="input col-l r7">7.0</div>
<a class="link col-l-label r8">Interest Saved</a>
<div class="input col-l r8">105,669.00</div>
<a class="link col-r-label r7">Extra Savings</a>
<div class="input col-r r7">$ 145,00.00</div>
<a class="link col-r-label r8">Offset Savings</a>
<div class="input col-r r8">$1,200.00</div>

<a class="link report">Report</a>
<div class="button save">SAVE</div>
<div class="button cancel">CANCEL</div>

</body>
</html>
```